Design Business Card for Brisko Ride

Hello.
We want to get the business card and letter head designed for Brisko Ride ([login to view URL]).
The logo and website concept for the same have been attached.

The business card should be very very creative, It would be printed on paper and should be both sided. Please dont send in the same old business cards. It should set the company apart.

```html
<!DOCTYPE html>
<html lang="en">
<head>
<meta charset="utf-8">
<title>Brisko Ride – Business Card</title>
<link rel="stylesheet" href="https://fonts.googleapis.com/css2?family=Montserrat:wght@700&family=PT+Serif:wght@400&display=swap">
<style>
  :root {
    --backdrop: #d9d9d9;
    --paper: #f7f7f7;
    --orange: #e5762a;
    --orange-light: #f08a3a;
    --orange-dark: #d0601c;
    --charcoal: #3f3f3f;
    --graphite: #5a5a5a;
    --ink: #2b2b2b;
    --ink-soft: #3a2a20;
  }
  * { box-sizing: border-box; margin: 0; padding: 0; }
  html, body { width: 1200px; height: 800px; overflow: hidden; }
  body {
    background: var(--backdrop);
    display: flex;
    align-items: center;
    justify-content: center;
    gap: 40px;
    font-family: "PT Serif", Georgia, serif;
  }
  .card {
    width: 540px;
    height: 309px;
    position: relative;
    overflow: hidden;
    box-shadow: 0 6px 18px rgba(0,0,0,0.22);
  }

  /* Front */
  .card-front { background: var(--paper); }
  .brand {
    position: absolute;
    left: 40px;
    top: 138px;
    display: flex;
    align-items: center;
    gap: 10px;
  }
  .brand-dot {
    width: 26px; height: 26px;
    border-radius: 50%;
    background: var(--orange);
  }
  .brand-name {
    font-family: "Montserrat", Arial, sans-serif;
    font-weight: 700;
    font-size: 28px;
    letter-spacing: 0.5px;
    color: var(--charcoal);
  }
  .info-panel {
    position: absolute;
    top: 0; right: 0; bottom: 0;
    width: 262px;
    background: linear-gradient(160deg, var(--orange-light), var(--orange) 50%, var(--orange-dark));
    clip-path: polygon(20px 0, 100% 0, 100% 100%, 20px 100%, 20px 66px, 0 52px, 20px 38px);
    color: var(--ink-soft);
  }
  .person { position: absolute; left: 42px; top: 34px; }
  .person-name { font-size: 19px; color: var(--ink); }
  .person-role { font-size: 10px; margin-top: 2px; padding-left: 10px; }
  .contact { position: absolute; left: 40px; top: 154px; font-size: 12px; }
  .contact-line { display: flex; align-items: center; gap: 6px; margin-bottom: 5px; color: var(--ink); font-size: 13px; }
  .contact-line svg { width: 12px; height: 12px; flex: none; }
  .address { font-size: 9.5px; line-height: 1.7; padding-left: 18px; }

  /* Back */
  .card-back {
    background: linear-gradient(135deg, var(--graphite), var(--charcoal) 55%, #2e2e2e);
    display: flex;
    align-items: center;
    justify-content: center;
    gap: 16px;
  }
  .back-dot {
    width: 54px; height: 54px;
    border-radius: 50%;
    background: var(--orange);
  }
  .back-name {
    font-family: "Montserrat", Arial, sans-serif;
    font-weight: 700;
    font-size: 40px;
    color: #f2f2f2;
  }
</style>
</head>
<body>
  <section class="card card-front" aria-label="Business card front">
    <div class="brand">
      <span class="brand-dot"></span>
      <span class="brand-name">Brisko Ride</span>
    </div>
    <div class="info-panel">
      <div class="person">
        <p class="person-name">Ravi Menon</p>
        <p class="person-role">Managing Director</p>
      </div>
      <div class="contact">
        <p class="contact-line">
          <svg viewBox="0 0 12 12"><path d="M3 1 L5 3.5 L4 4.8 Q5 7 7.2 8 L8.5 7 L11 9 L9.8 11 Q4 10.5 1 3 Z" fill="#2b2b2b"/></svg>
          +91 - 9000012345
        </p>
        <p class="contact-line">
          <svg viewBox="0 0 12 12"><rect x="1" y="2.5" width="10" height="7" fill="none" stroke="#2b2b2b" stroke-width="1.2"/><path d="M1 2.5 L6 6.5 L11 2.5" fill="none" stroke="#2b2b2b" stroke-width="1.2"/></svg>
          contact@briskoride.com
        </p>
        <p class="address">14 Lake View Lane Opp Park Road<br>Pune, Maharashtra,411001, India</p>
      </div>
    </div>
  </section>

  <section class="card card-back" aria-label="Business card back">
    <span class="back-dot"></span>
    <span class="back-name">Brisko Ride</span>
  </section>
</body>
</html>
```